Flyer für Weingut
Zielgruppe
Wir sind das Familien Weingut Kolbe aus der Südpalz und wohnen direkt in der Holunderstraße. Eine Straße die viele Touristen anzieht. Wir möchten dieses Jahr das erste mal einen art Gutsauschank eröffnen. Indem es kleinigkeiten zu Essen und unseren Wein zu trinken gibt. Wir möchten sowohl die Touristen einfangen aber auch vorallem einheimische aus den nachbar Orten als Kunden gewinnen. Jeder ist willkomen von jung bis alt.
Aufgabenstellung
modern, ansprechend, professionell, klar, strukuriert, besonders.
Öffnungszeiten unseres Ausschanks: Mittwoch bis Sonntag ab 22.08.25 bis 02.11.25 von 14-20 Uhr
Es gibts kleinigkeiten zu essen zum beispiel Flammkuchen, Pfälzer Tapas oder auch Gemische Wurst/Käse Platten. Getränke: Offene Weine oder Flaschenweine, Weinschorle. Die Essensauswahl soll nicht genaustens aufgelistet werden. Es reicht zum Beispiel: Kleinigkeiten zum Essen oder ähnliches.
Zusatzinfos: Kleiner Hof mit Gartenmöbel. Platz für ca. 50 Leute. Kleine Louge Ecke mit Loungemöbeln. Es gibt nur Selbstbedienung. Gemütliche, lockere Atmosphäre. Vielfältige Weinauswahl.
Wir möchten speziell von Mischgetränken Abstand nehmen. Wir als Familienweingut stehen hinter unserem Produkt und möchten vorallem auch den jungen Leuten den Wein wieder näher bringen. Wir haben Ihnen unten auch ein paar Beispiele hochgeladen in welche Richtung es gehen könnte.
Wichtrig ist das auf unserem Flyer die Kontakdaten, Adresse sowie Instagramname zu finden sind. Nicht sehr groß unjd presänt am besten in einer Ecke.
Unser Logo sollte zu sehen sein. Muss aber nicht unbedingt in den Vordergrund. Die Zeiten sowie Essen und Getränke. Oder anstatt die Getränke gleich eine passende Überschrift wie Gutsauschank oder ähnliches. Auch ein entworfenes Logo wie unten in den Beispielen könnten wir uns vorstellen.
Der flyer allgemein sollte nicht all zu viel Text haben.

```html
<!DOCTYPE html>
<html lang="de">
<head>
<meta charset="utf-8">
<title>Gutsausschank 2025 – Weingut Kolbe</title>
<link rel="stylesheet" href="https://fonts.googleapis.com/css2?family=Alegreya+Sans:ital,wght@0,400;0,700;0,800;1,400&family=Raleway:wght@800&display=swap">
<style>
  :root {
    --stripe: #d6c1cb;
    --paper: #ffffff;
    --grape: #6f3250;
    --ink: #111111;
    --backdrop: #f3f1f2;
  }
  html, body {
    margin: 0;
    width: 750px;
    height: 1200px;
    overflow: hidden;
    background: var(--backdrop);
  }
  .flyer {
    position: absolute;
    left: 75px;
    top: 0;
    width: 600px;
    height: 1200px;
    display: block;
  }
  .paper { fill: var(--paper); }
  .stripe { fill: var(--stripe); }
  .headline {
    font-family: "Raleway", sans-serif;
    font-weight: 800;
    font-size: 96px;
    letter-spacing: 2px;
    fill: var(--ink);
  }
  .side-label {
    font-family: "Alegreya Sans", sans-serif;
    font-size: 36px;
    fill: var(--ink);
  }
  .grape-art { fill: var(--grape); }
  .frame line { stroke: var(--ink); stroke-width: 5; }
  .year {
    font-family: "Alegreya Sans", sans-serif;
    font-size: 50px;
    letter-spacing: 16px;
    fill: var(--ink);
  }
  .tagline {
    font-family: "Alegreya Sans", sans-serif;
    font-style: italic;
    font-size: 38px;
    fill: var(--ink);
  }
  .schedule {
    font-family: "Alegreya Sans", sans-serif;
    font-size: 38px;
    fill: var(--ink);
  }
  .divider { stroke: var(--ink); stroke-width: 6; }
  .brand-name {
    font-family: "Alegreya Sans", sans-serif;
    font-weight: 800;
    font-size: 74px;
    letter-spacing: 6px;
    fill: var(--ink);
  }
  .address {
    font-family: "Alegreya Sans", sans-serif;
    font-size: 30px;
    fill: var(--ink);
  }
  .website {
    font-family: "Alegreya Sans", sans-serif;
    font-weight: 700;
    font-size: 29px;
    fill: var(--ink);
  }
</style>
</head>
<body>
<svg class="flyer" viewBox="0 0 944 1888" xmlns="http://www.w3.org/2000/svg">
  <defs>
    <path id="headline-arc" d="M 132 546 A 340 340 0 0 1 812 546"/>
  </defs>

  <rect class="paper" x="0" y="0" width="944" height="1888"/>

  <g class="stripes">
    <polygon class="stripe" points="230,0 735,0 0,735 0,230"/>
    <polygon class="stripe" points="944,218 944,723 0,1667 0,1162"/>
    <polygon class="stripe" points="944,1150 944,1656 712,1888 206,1888"/>
  </g>

  <text class="headline">
    <textPath href="#headline-arc" startOffset="50%" text-anchor="middle">GUTSAUSSCHANK</textPath>
  </text>

  <text class="side-label" x="110" y="570">WEINGUT</text>
  <text class="side-label" x="834" y="570" text-anchor="end">KOLBE</text>

  <rect class="grape-art" x="360" y="346" width="236" height="296" rx="110"
        role="img" aria-label="Illustration einer Weintraube mit Weinblatt"/>

  <g class="frame">
    <line x1="115" y1="656" x2="115" y2="1806"/>
    <line x1="829" y1="656" x2="829" y2="1806"/>
    <line x1="112.5" y1="1804" x2="306" y2="1804"/>
    <line x1="638" y1="1804" x2="831.5" y2="1804"/>
  </g>

  <text class="year" x="480" y="750" text-anchor="middle">2025</text>

  <text class="tagline" text-anchor="middle">
    <tspan x="472" y="850">Pfälzer Weine aus eigenem Anbau &amp;</tspan>
    <tspan x="472" y="899">regionale Köstlichkeiten</tspan>
  </text>

  <text class="schedule" text-anchor="end">
    <tspan x="435" y="1288">22. August</tspan>
    <tspan x="435" y="1337">bis</tspan>
    <tspan x="435" y="1386">2. November</tspan>
  </text>
  <line class="divider" x1="472" y1="1238" x2="472" y2="1408"/>
  <text class="schedule">
    <tspan x="511" y="1288">Jeden Mittwoch</tspan>
    <tspan x="511" y="1337">bis Sonntag</tspan>
    <tspan x="511" y="1386">14 – 20 Uhr</tspan>
  </text>

  <text class="brand-name" x="475" y="1592" text-anchor="middle">KOLBE</text>

  <text class="address" text-anchor="middle">
    <tspan x="472" y="1683">Holunderstr. 62</tspan>
    <tspan x="472" y="1722">76899 Rebenhausen / Weinstraße</tspan>
  </text>

  <text class="website" x="472" y="1813" text-anchor="middle">www.wein-kolbe.de</text>
</svg>
</body>
</html>
```